BOLD Gym Needs a New WALL WRAP!

We have a small wall that we need to spice up and we'd like to wrap it with a bold design that stands out and breaks up the current bland grey color.
The wall itself is 128.25" long x 50.5" tall
I am open to design options, but the design must include our ZorvaLyft logo (attached)
I have also included photos of the gym to give you an idea of the vibe, colors, etc.
DO NOT BE AFRAID OF COLOR😊​ Although our colors are Yellow, Grey's, Blacks, etc., in the gym, please do not be afraid to play with color while still making it look like it belongs in our building. The posters that hang around that wall have pinks, purples, etc. in it. I've included a poster for you to see the colors that are nearby.
The photo from the ground looking up towards the second story highlights the wall that needs to be wrapped.
The ultimate goal here is to break up the grey wall with a killer design.

```html
<!DOCTYPE html>
<html lang="en">
<head>
<meta charset="utf-8">
<title>ZorvaLyft Wall Wrap</title>
<link rel="stylesheet" href="https://fonts.googleapis.com/css2?family=Anton&family=Montserrat:wght@700&display=swap">
<style>
  :root {
    --stage: #333333;
    --black: #000000;
    --band-grey: #3d3c40;
    --yellow: #f7cf00;
    --white: #ffffff;
  }
  html, body {
    margin: 0;
    padding: 0;
    width: 1200px;
    height: 780px;
    overflow: hidden;
    background: var(--stage);
  }
  .canvas {
    position: relative;
    width: 1200px;
    height: 780px;
  }
  .wall-wrap {
    position: absolute;
    left: 166px;
    top: 87px;
    width: 870px;
    height: 343px;
    display: block;
    box-shadow: 14px 16px 22px rgba(0, 0, 0, 0.45);
  }
  .wordmark {
    font-family: "Anton", "Oswald", sans-serif;
    fill: var(--white);
    letter-spacing: 0.5px;
  }
  .headline {
    font-family: "Montserrat", "Helvetica Neue", Arial, sans-serif;
    font-weight: 700;
    font-size: 46px;
  }
  .headline .accent { fill: var(--yellow); }
  .headline .mark { fill: var(--white); }
  .brand-lockup {
    position: absolute;
    left: 401px;
    top: 548px;
    width: 400px;
    margin: 0;
    font-family: "Anton", "Oswald", sans-serif;
    font-weight: 400;
    font-size: 112px;
    line-height: 1;
    color: var(--white);
    text-align: center;
    letter-spacing: 1px;
  }
</style>
</head>
<body>
<main class="canvas">
  <svg class="wall-wrap" viewBox="0 0 870 343" xmlns="http://www.w3.org/2000/svg">
    <defs>
      <radialGradient id="photo-tone" cx="0.5" cy="0.45" r="0.6">
        <stop offset="0" stop-color="#3a3a3a"/>
        <stop offset="0.6" stop-color="#161616"/>
        <stop offset="1" stop-color="#050505"/>
      </radialGradient>
    </defs>

    <!-- base panels -->
    <rect class="panel-left" x="0" y="0" width="419" height="343" fill="var(--black)"/>
    <rect class="panel-photo" x="419" y="0" width="258" height="343" fill="url(#photo-tone)"
          role="img" aria-label="Black and white photo of a muscular athlete curling a barbell"/>
    <rect class="panel-band" x="677" y="0" width="111" height="343" fill="var(--band-grey)"/>
    <rect class="panel-right" x="788" y="0" width="82" height="343" fill="var(--black)"/>

    <!-- corner blocks -->
    <polygon class="corner-yellow-top" points="770,0 870,0 870,77 834,77" fill="var(--yellow)"/>
    <polygon class="corner-white-bottom" points="771,266 807,266 870,343 771,343" fill="var(--white)"/>
    <polygon class="corner-yellow-left" points="0,230 88,230 88,272 0,343" fill="var(--yellow)"/>

    <!-- brand name -->
    <text class="wordmark" x="118" y="173" font-size="66" textLength="228" lengthAdjust="spacingAndGlyphs">ZorvaLyft</text>

    <!-- plate bars -->
    <g class="plate-bars-white" fill="var(--white)">
      <polygon points="135,217 198,156 208,164 144,224"/>
      <polygon points="160,228 208,177 218,188 169,236"/>
      <polygon points="189,232 210,208 220,217 197,238"/>
    </g>
    <g class="plate-bars-yellow" fill="var(--yellow)">
      <polygon points="249,227 265,228 262,314 246,313"/>
      <rect x="270" y="236" width="15" height="69"/>
      <rect x="294" y="252" width="11" height="35"/>
    </g>

    <!-- headline -->
    <g class="headline">
      <rect class="mark" x="377" y="101" width="9" height="68"/>
      <text class="mark" x="376" y="135">P</text>
      <text class="accent" x="419" y="135" textLength="159" lengthAdjust="spacing">ERSO</text>
      <rect class="mark" x="614" y="58" width="8" height="77"/>
      <text class="mark" x="590" y="135">N</text>
      <text class="accent" x="634" y="135">A</text>
      <rect class="accent-line" x="684" y="101" width="9" height="34" fill="var(--yellow)"/>
      <rect class="accent-line" x="684" y="128" width="96" height="7" fill="var(--yellow)"/>

      <text class="accent" x="435" y="187" textLength="217" lengthAdjust="spacing">GROUP</text>

      <rect class="mark" x="400" y="209" width="9" height="79"/>
      <text class="mark" x="388" y="240">T</text>
      <text class="accent" x="431" y="240" textLength="171" lengthAdjust="spacing">RAINI</text>
      <rect class="mark" x="618" y="209" width="8" height="79"/>
      <text class="mark" x="617" y="240">N</text>
      <text class="accent" x="662" y="240">G</text>
    </g>
  </svg>

  <p class="brand-lockup">ZorvaLyft</p>
</main>
</body>
</html>
```